Letterhead and invoice

Simple design for letterhead and invoice document (2 separate files). Must be word and excel compatible.

Must use logo (attached)
ABN: 47 209 851 624
Address: 14 Marrick Crescent, Tolland NSW
Phone: 0417263948

Target Market(s)

Professional

Industry/Entity Type

Invoice

Font styles to use
Serif
Sans Serif

Colors

Designer to choose colors to be used in the design.

Requirements
Must have
• As above

```html
<!DOCTYPE html>
<html lang="en">
<head>
<meta charset="utf-8">
<title>Kestrel Civil Letterhead</title>
<link href="https://fonts.googleapis.com/css2?family=Archivo:wght@400;800&display=swap" rel="stylesheet">
<style>
  :root {
    --backdrop: #dcdddf;
    --paper: #ffffff;
    --ink: #1a1a1a;
    --brand-red: #e2231a;
    --rule-grey: #e3e3e3;
    --tint: #fcefea;
  }
  * { box-sizing: border-box; margin: 0; padding: 0; }
  html, body { width: 1200px; height: 838px; overflow: hidden; }
  body {
    background: var(--backdrop);
    font-family: "Archivo", Arial, sans-serif;
    color: var(--ink);
    position: relative;
  }
  .sheet {
    position: absolute;
    top: 51px;
    width: 520px;
    height: 735px;
    background: var(--paper);
    box-shadow: 0 1px 5px rgba(0,0,0,0.22);
  }
  .sheet--ruled { left: 51px; }
  .sheet--linear { left: 616px; }

  .brand {
    position: absolute;
    left: 26px;
    top: 27px;
    display: flex;
    align-items: center;
    gap: 8px;
  }
  .brand__square {
    width: 24px; height: 24px;
    background: var(--brand-red);
  }
  .brand__name {
    font-weight: 800;
    font-size: 14px;
    letter-spacing: 0.2px;
    text-transform: uppercase;
    line-height: 1;
  }

  .contact {
    position: absolute;
    font-size: 7.6px;
    line-height: 10px;
    text-align: right;
    white-space: nowrap;
  }
  .contact__label { color: var(--brand-red); }
  .sheet--ruled .contact { right: 26px; top: 26px; }
  .sheet--linear .contact { right: 26px; top: 27px; line-height: 16px; }
  .contact__gap { display: inline-block; width: 8px; }

  .rule {
    position: absolute;
    left: 26px;
    right: 24px;
    height: 3px;
    background: var(--rule-grey);
  }
  .rule--top { top: 114px; }
  .rule--bottom { top: 700px; }

  .header-line {
    position: absolute;
    left: 228px;
    width: 266px;
    top: 38px;
    height: 1px;
    background: var(--rule-grey);
  }

  .backdrop-mark {
    position: absolute;
    width: 178px;
    height: 178px;
    background: var(--tint);
  }
  .sheet--ruled .backdrop-mark { left: 171px; top: 294px; }
  .sheet--linear .backdrop-mark { left: 171px; top: 291px; }
</style>
</head>
<body>
  <section class="sheet sheet--ruled">
    <div class="brand">
      <span class="brand__square"></span>
      <span class="brand__name">Kestrel Civil</span>
    </div>
    <div class="contact">
      <div>14 Marrick Crescent, Tolland NSW</div>
      <div><span class="contact__label">P:</span> 0417263948</div>
      <div><span class="contact__label">ABN:</span> 47 209 851 624</div>
    </div>
    <div class="rule rule--top"></div>
    <div class="backdrop-mark"></div>
    <div class="rule rule--bottom"></div>
  </section>

  <section class="sheet sheet--linear">
    <div class="brand">
      <span class="brand__square"></span>
      <span class="brand__name">Kestrel Civil</span>
    </div>
    <div class="header-line"></div>
    <div class="contact">
      <div>14 Marrick Crescent, Tolland NSW</div>
      <div><span class="contact__label">P:</span> 0417263948<span class="contact__gap"></span><span class="contact__label">ABN:</span> 47 209 851 624</div>
    </div>
    <div class="backdrop-mark"></div>
  </section>
</body>
</html>
```